Halt and Thrive Hair Product Labels

We need a new label designed for a hair growth product. We are a US company that has created a revolutionary new cure for hereditary hair loss based on precision medicine.

Our new product is very different to all other hair loss products on the market in that it actually really works. Unfortunately there is no requirement in the US for truth in advertising by products that are not regulated by the FDA. We use only FDA approved active ingredients.

We want a fresh, new design to reflect this exciting product but also to demonstrate that it is medicine and it is regulated and not a fake product trying to scam people.

The Halt and reThrive topical hair solution is suspended in a ground-breaking foam or serum water based solution that does not cause scalp irritation and takes just seconds to apply each night before bed.

We would like to see a design that is modern, simple and bold, and includes our corporate colors in particular the green.

Brand colors: white, green #4ca26f, light blue #46b1d7, light grey #999999, dark grey #262626
See our website for more details: http://www.haltandthrive.example/

The final design should communicate health and well-being.

Note we had a previous set of labels which I have uploaded for reference, but these were based on our old logo. We have since created a new logo and so now need updated logos to reflect the new logo, colors and branding.

There are 2 product types for this label – Topical Solution and Pills each with different sizes.
Similar label design for both product variations. Just adjust sizing and some of the content.

Dimensions for labels:
1. Topical solution (2 variations) - 4 inches width (wraps the bottle to provide a front and back side) x 2 inches H
2. Pills (2 variations) – 3.5 inches width (also wraps) x 2 inches width

Attached:
Company name and logo to go onto label
I also attached examples of the old label based on our old logo. Not because you should follow that but just for background.
We are not open to an update of the logo or colors as part of the project.

Information to go on label:
See below for detailed for each label.

Target Market
Males between 20-45 years.

Health and well-being, modern, organic, forward thinking look And feel
Modern, Professional, Upmarket, Bold, Serious, New Generation, Precision Medicine.
We have a lot of male customers who are scared of medicines and chemicals so we don’t want the brand to look like it includes harsh chemicals or anything like that. We compound so we don’t have to include any preservatives etc in our products.

Label 1 - Hair Topical – Foam variation
2 inches tall x 4 inches wide

Front (information to be included):
Logo: Halt and Thrive (you cannot change the layout of the logo)
Personalized Topical Hair Solution
FDA Approved Ingredients in Proprietary Activation Base
Proprietary Compounded Formula Based on Your DNA

Back (information to be included):
Directions
Activate Solution Prior To Each Use By Shaking well
Apply Up to One Pump Nightly Before Bed
Each Bottle To Last 3 Months

Please call (555) 284-9163 for Refills

Important
This medicine has been created by Calvin Brisbane MD following the Halt and Thrive personalized program to Stop your hair loss and Regrow your own hair. The formula is personalized just for you based on your cause of hair loss, DNA and personal biology.
Do Not Share with others as each person’s hair loss, biology and DNA are different.

Label 2 - Hair Topical – Serum variation
2 inches tall x 3.5 inches wide

Logo: Halt and Thrive

Directions
Apply Up to Seven (7) Drops Nightly Before Bed To Affected Areas of the Scalp (also want a variation that says: Apply Up to Eleven (11) Drops...)

Important

Label 3 - Dutasteride Capsules

Information to be included:
Logo: Halt and Thrive
Compounded Dutasteride to Block Circulating DHT
Personalized Hair Dose Based on Your DNA 0.7mg
Take 1 x Capsule Daily

Label 4 - Finoral Capsules

Logo: Halt and Thrive
Other verbiage to be included:
Compounded Dutasteride to Block Circulating DHT Plus Anastrazole to Block Conversion to Estrogen
Personalized Dose Based on Your DNA: DT 0.7mg + AZ 0.2mg
Take 1 x Capsule Daily
Updates

Hello designers! I have extended the timeline for this project because we are looking for new different designs to the ones we had previously. This was not a project to simply replace the logo and have the same layout and design, I included the previous design for reference of the information included not for design/style. It was made to suit the old logo. Now we have a new logo we need a new completely different design to match that logo. If you are interested in participating in this contest it would be great if you could please submit new and original design ideas for me to select from. I will not select a design that is the same as the previous one. Thanks so much! Marnie

Target Market(s)

Males 20 to 45

Industry/Entity Type

Health And Wellness

Font styles to use
Sans Serif

Colors
00a990
ffffff
333333
cfcfcf

Requirements
Must have
• Must use our logo and brand colors
Should not have
• Don't use any red except for warnings

```html
<!DOCTYPE html>
<html lang="en">
<head>
<meta charset="utf-8">
<title>Halt and reThrive – Label Set</title>
<link href="https://fonts.googleapis.com/css2?family=Antonio:wght@400;600;700&family=Pathway+Gothic+One&family=Montserrat:wght@400;500&display=swap" rel="stylesheet">
<style>
  :root{
    --stage:#3a3a3a;
    --ink:#2f2f2f;
    --green:#128166;
    --white:#ffffff;
    --rule:rgba(255,255,255,.55);
    --soft:#cfcfcf;
    --head:"Antonio", sans-serif;
    --body:"Pathway Gothic One", sans-serif;
    --brand:"Montserrat", sans-serif;
  }
  *{box-sizing:border-box;margin:0;padding:0}
  html,body{width:1200px;height:880px;overflow:hidden;background:var(--stage)}
  .canvas{position:relative;width:1200px;height:880px}

  /* label shell */
  .label{position:absolute;background:var(--white);display:flex;padding:16px 0 0 15px;height:274px}
  .label--serum{left:90px;top:154px;width:517px}
  .label--foam{left:90px;top:446px;width:517px}
  .label--pills{left:652px;top:153px;width:458px;padding-left:16px;padding-top:15px}
  .label--capsule{left:652px;top:451px;width:458px;padding-left:16px;padding-top:15px}

  .front,.back{position:relative;height:241px;background:var(--ink);color:var(--white);overflow:hidden}
  .label--foam .front,.label--foam .back,
  .label--capsule .front,.label--capsule .back{background:var(--green)}
  .label--serum .front,.label--foam .front{width:230px}
  .label--serum .back,.label--foam .back{width:228px}
  .label--pills .front,.label--capsule .front{width:198px;height:242px}
  .label--pills .back,.label--capsule .back{width:203px;height:242px}

  /* wrap band */
  .band{width:26px;height:241px;background:var(--green);color:var(--white);display:flex;align-items:center;justify-content:center}
  .label--foam .band,.label--capsule .band{background:var(--ink)}
  .label--pills .band,.label--capsule .band{width:24px;height:242px}
  .band__inner{writing-mode:vertical-rl;transform:rotate(180deg);display:flex;align-items:center;gap:4px;height:220px}
  .band__seal{display:flex;align-items:center;gap:2px}
  .band__square{width:13px;height:13px;border:2px solid var(--white)}
  .band__approved{font:600 5px var(--head);letter-spacing:.3px}
  .band__text{font:700 8.6px/1.15 var(--head);letter-spacing:.2px;text-transform:uppercase}

  /* brand block */
  .logo-tab{position:absolute;left:0;top:0;width:206px;height:61px;background:var(--white);border-bottom-right-radius:22px}
  .brand-mark{position:absolute;left:26px;top:12px;width:38px;height:38px;border-radius:50%;background:var(--ink)}
  .label--foam .brand-mark{background:var(--green)}
  .label--pills .brand-mark,.label--capsule .brand-mark{left:14px;top:13px;background:var(--white)}
  .brand-name{position:absolute;left:82px;top:16px;font:500 14px var(--brand);color:var(--ink);white-space:nowrap}
  .label--foam .brand-name{color:var(--green)}
  .label--pills .brand-name,.label--capsule .brand-name{left:66px;top:18px;color:var(--white)}
  .brand-rule{position:absolute;left:82px;top:37px;width:116px;height:1px;background:var(--soft)}
  .label--pills .brand-rule,.label--capsule .brand-rule{left:66px;top:38px;width:115px;background:var(--rule)}
  .brand-by{position:absolute;left:82px;top:42px;font:400 9px var(--brand);color:var(--ink);white-space:nowrap}
  .label--foam .brand-by{color:var(--green)}
  .label--pills .brand-by,.label--capsule .brand-by{left:66px;top:44px;color:var(--white)}

  /* topical front */
  .personalized{position:absolute;left:30px;top:77px;width:34px;height:125px;border:1.5px solid var(--white);display:flex;align-items:center;justify-content:center}
  .personalized span{writing-mode:vertical-rl;transform:rotate(180deg);font:400 21px var(--head);letter-spacing:1px}
  .headline-top{position:absolute;left:71px;top:75px;font:400 25px/1 var(--head);transform:scaleY(1.6);transform-origin:top left;white-space:nowrap}
  .headline-main{position:absolute;left:69px;top:114px;font:400 58px/1 var(--head);transform:scaleY(1.55);transform-origin:top left;letter-spacing:-1px;white-space:nowrap}
  .label--foam .headline-main{font-size:62px;transform:scaleY(1.45)}
  .tagline{position:absolute;left:30px;top:203px;font:400 11.5px var(--body);white-space:nowrap}
  .volume{position:absolute;left:178px;top:220px;width:24px;height:21px;background:var(--white);border-radius:6px 6px 0 0;color:var(--ink);font:500 7.5px/1 var(--brand);text-align:center;padding-top:3px}
  .volume small{display:block;font-size:6px}

  /* oral front */
  .product-shape{position:absolute;left:0;top:69px;width:186px;height:120px;background:var(--white);border-radius:0 60px 60px 0}
  .oral-kicker{position:absolute;left:14px;top:85px;font:400 18px/1 var(--head);color:var(--green);transform:scaleY(1.45);transform-origin:top left;white-space:nowrap}
  .oral-title{position:absolute;left:14px;top:112px;font:400 42px/1 var(--head);color:var(--green);transform:scaleY(1.75);transform-origin:top left;letter-spacing:-1px}
  .pill-icon{position:absolute;left:115px;top:110px;width:23px;height:62px;border-radius:12px;overflow:hidden;border:2px solid var(--ink);display:flex;flex-direction:column}
  .pill-icon i{flex:1;background:var(--ink)}
  .pill-icon i+i{background:var(--green);border-top:2px solid var(--white)}
  .label--capsule .oral-kicker{top:96px;font-size:19px;color:var(--ink);transform:scaleY(1.5)}
  .label--capsule .oral-title{top:124px;font-size:46px;color:var(--ink);transform:scaleY(1.55)}
  .capsule-icon{position:absolute;left:75px;top:101px;width:63px;height:22px;border-radius:11px;overflow:hidden;display:flex}
  .capsule-icon i{flex:1;background:var(--green)}
  .capsule-icon i+i{background:var(--ink);border-left:2px solid var(--white)}
  .oral-note{position:absolute;left:16px;top:198px;font:400 11px/14px var(--body);white-space:nowrap}
  .label--capsule .oral-note{top:193px}
  .oral-count{position:absolute;left:16px;top:224px;font:400 12px var(--brand)}

  /* back panel: every block placed on the panel grid */
  .back > *{position:absolute;left:19px;white-space:nowrap}
  .label--pills .back > *,.label--capsule .back > *{left:9px}
  .dose{top:9px;font:400 12px/13px var(--body)}
  .section-title{font:400 14px/1 var(--body);text-transform:uppercase}
  .title-directions{top:11px}
  .label--pills .title-directions{top:47px}
  .label--capsule .title-directions{top:45px}
  .steps{top:28px;list-style:none;font:400 10px/13px var(--body)}
  .steps li{padding-left:6px;text-indent:-6px}
  .steps li::before{content:"• "}
  .plain-step{top:64px;font:400 11.5px/1 var(--body)}
  .rule{width:190px;height:1px;background:var(--rule)}
  .rule--a{top:60px}
  .rule--b{top:108px}
  .label--pills .rule--a,.label--capsule .rule--a{top:82px}
  .label--pills .rule--b,.label--capsule .rule--b{top:113px}
  .supply{top:65px;font:400 15px/1 var(--head);transform:scaleX(.64);transform-origin:left top}
  .refill{top:83px;font:400 18px/1 var(--head);transform:scaleX(.7);transform-origin:left top}
  .label--pills .refill,.label--capsule .refill{top:89px}
  .title-important{top:113px}
  .label--pills .title-important,.label--capsule .title-important{top:120px}
  .note{top:129px;width:192px;white-space:normal;font:400 10.3px/12.2px var(--body)}
  .label--pills .note,.label--capsule .note{top:135px;width:190px}
  .share{top:204px;bottom:0;left:22px !important;width:183px;background:var(--white);border-radius:8px 8px 0 0;color:var(--green);font:400 11px/14px var(--body);text-align:center;padding-top:5px}
  .label--foam .share{color:var(--ink)}
  .label--pills .share,.label--capsule .share{left:10px !important}
</style>
</head>
<body>
<main class="canvas">

  <!-- Serum -->
  <section class="label label--serum">
    <div class="front">
      <div class="logo-tab">
        <span class="brand-mark"></span>
        <span class="brand-name">Halt &amp; reThrive</span>
        <span class="brand-rule"></span>
        <span class="brand-by">by Calvin Brisbane M.D.</span>
      </div>
      <div class="personalized"><span>PERSONALIZED</span></div>
      <div class="headline-top">HAIR TOPICAL</div>
      <div class="headline-main">SERUM</div>
      <p class="tagline">Proprietary Compounded Formula Based on Your DNA</p>
      <div class="volume">50<small>mL</small></div>
    </div>
    <div class="band">
      <div class="band__inner">
        <div class="band__seal"><span class="band__square"></span><span class="band__approved">APPROVED</span></div>
        <p class="band__text">Active ingredients in proprietary<br>activation base</p>
      </div>
    </div>
    <div class="back">
      <h3 class="section-title title-directions">Directions</h3>
      <ul class="steps"><li>Apply Up to Eleven Drops Nightly Before Bed To<br>Affected Areas of the Scalp.</li></ul>
      <div class="rule rule--a"></div>
      <p class="supply">Each Bottle To Last 3 Months</p>
      <p class="refill">Please call (555) 284-9163 for Refills</p>
      <div class="rule rule--b"></div>
      <h3 class="section-title title-important">Important</h3>
      <p class="note">This medicine has been created by Calvin Brisbane MD following the Halt and reThrive personalized program to Stop your hair loss and reGrow your own hair. The formula is personalized just for you based on your cause of hair loss, DNA and personal biology.</p>
      <p class="share">Do Not Share with others as each person's hair loss,<br>biology and DNA are different.</p>
    </div>
  </section>

  <!-- Foam -->
  <section class="label label--foam">
    <div class="front">
      <div class="logo-tab">
        <span class="brand-mark"></span>
        <span class="brand-name">Halt &amp; reThrive</span>
        <span class="brand-rule"></span>
        <span class="brand-by">by Calvin Brisbane M.D.</span>
      </div>
      <div class="personalized"><span>PERSONALIZED</span></div>
      <div class="headline-top">HAIR TOPICAL</div>
      <div class="headline-main">FOAM</div>
      <p class="tagline">Proprietary Compounded Formula Based on Your DNA</p>
      <div class="volume">50<small>mL</small></div>
    </div>
    <div class="band">
      <div class="band__inner">
        <div class="band__seal"><span class="band__square"></span><span class="band__approved">APPROVED</span></div>
        <p class="band__text">Active ingredients in proprietary<br>activation base</p>
      </div>
    </div>
    <div class="back">
      <h3 class="section-title title-directions">Directions</h3>
      <ul class="steps">
        <li>Activate Solution Prior To Each Use By Shaking well.</li>
        <li>Apply Up to One Pump Nightly Before Bed.</li>
      </ul>
      <div class="rule rule--a"></div>
      <p class="supply">Each Bottle To Last 3 Months</p>
      <p class="refill">Please call (555) 284-9163 for Refills</p>
      <div class="rule rule--b"></div>
      <h3 class="section-title title-important">Important</h3>
      <p class="note">This medicine has been created by Calvin Brisbane MD following the Halt and reThrive personalized program to Stop your hair loss and reGrow your own hair. The formula is personalized just for you based on your cause of hair loss, DNA and personal biology.</p>
      <p class="share">Do Not Share with others as each person's hair loss,<br>biology and DNA are different.</p>
    </div>
  </section>

  <!-- Dutasteride pills -->
  <section class="label label--pills">
    <div class="front">
      <span class="brand-mark"></span>
      <span class="brand-name">Halt &amp; reThrive</span>
      <span class="brand-rule"></span>
      <span class="brand-by">by Calvin Brisbane M.D.</span>
      <div class="product-shape"></div>
      <div class="oral-kicker">DUTASTERIDE</div>
      <div class="oral-title">PILLS</div>
      <div class="pill-icon"><i></i><i></i></div>
      <p class="oral-note">Compounded Dutasteride to Block Circulating DHT</p>
      <p class="oral-count">90 PILLS</p>
    </div>
    <div class="band">
      <div class="band__inner">
        <div class="band__seal"><span class="band__square"></span><span class="band__approved">APPROVED</span></div>
        <p class="band__text">Only the actives - compounded<br>FDA approved active ingredients</p>
      </div>
    </div>
    <div class="back">
      <p class="dose">Personalized Hair Dose<br>Based on Your DNA: 0.5mg</p>
      <h3 class="section-title title-directions">Directions</h3>
      <p class="plain-step">Take 1 x Pill Daily With Protein.</p>
      <div class="rule rule--a"></div>
      <p class="refill">Please call (555) 284-9163 for Refills</p>
      <div class="rule rule--b"></div>
      <h3 class="section-title title-important">Important</h3>
      <p class="note">This medicine has been created by Calvin Brisbane MD following the Halt and reThrive personalized program to Stop your hair loss and reGrow your own hair. The formula is personalized just for you based on your cause of hair loss, DNA and personal biology.</p>
      <p class="share">Do Not Share with others as each person's hair loss,<br>biology and DNA are different.</p>
    </div>
  </section>

  <!-- Finoral capsules -->
  <section class="label label--capsule">
    <div class="front">
      <span class="brand-mark"></span>
      <span class="brand-name">Halt &amp; reThrive</span>
      <span class="brand-rule"></span>
      <span class="brand-by">by Calvin Brisbane M.D.</span>
      <div class="product-shape"></div>
      <div class="oral-kicker">FINORAL</div>
      <div class="capsule-icon"><i></i><i></i></div>
      <div class="oral-title">CAPSULE</div>
      <p class="oral-note">Compounded Dutasteride to Block Circulating DHT<br>Plus Anastrazole to Block Conversion to Estrogen</p>
      <p class="oral-count">90 PILLS</p>
    </div>
    <div class="band">
      <div class="band__inner">
        <div class="band__seal"><span class="band__square"></span><span class="band__approved">APPROVED</span></div>
        <p class="band__text">Only the actives - compounded<br>FDA approved active ingredients</p>
      </div>
    </div>
    <div class="back">
      <p class="dose">Personalized Dose Based on Your<br>DNA: DT 0.7mg + AZ 0.2mg</p>
      <h3 class="section-title title-directions">Directions</h3>
      <p class="plain-step">Take 1 x Capsule Daily</p>
      <div class="rule rule--a"></div>
      <p class="refill">Please call (555) 284-9163 for Refills</p>
      <div class="rule rule--b"></div>
      <h3 class="section-title title-important">Important</h3>
      <p class="note">This medicine has been created by Calvin Brisbane MD following the Halt and reThrive personalized program to Stop your hair loss and reGrow your own hair. The formula is personalized just for you based on your cause of hair loss, DNA and personal biology.</p>
      <p class="share">Do Not Share with others as each person's hair loss,<br>biology and DNA are different.</p>
    </div>
  </section>

</main>
</body>
</html>
```